Labor Day Sale Website Banner For High End Jewelry Website

We need a banner for our website (brindlyx.com) for a Labor Day Sale. The banner should be a size 1187 × 400. I have included a few pieces of jewelry to be included in the banner (do not need to use all, can use just some). The banner should say:
"Labor Day Sale"
"Save 15% on Everything!"
Use Promo Code: HALCYON

Target Market(s)

Affluent Female Consumers

Industry/Entity Type

Jewelry

Colors

Designer to choose colors to be used in the design.

```html
<!DOCTYPE html>
<html lang="en">
<head>
<meta charset="utf-8">
<title>Brindlyx – Labor Day Sale</title>
<link rel="stylesheet" href="https://fonts.googleapis.com/css2?family=Open+Sans:wght@400;600&display=swap">
<style>
  :root {
    --white: #ffffff;
    --ink: #1a1a1a;
    --plum: #6a2a45;
    --lav-1: #e7d9ec;
    --lav-2: #d9c3e3;
    --pink-1: #efd3e4;
    --gem-violet: #6d5a9c;
    --gem-gold: #b68d3a;
    --ring-dark: #3f2f52;
  }
  * { margin: 0; padding: 0; box-sizing: border-box; }
  html, body { width: 1200px; height: 404px; overflow: hidden; background: var(--white); }
  .banner {
    position: relative;
    width: 1200px;
    height: 404px;
    font-family: "Open Sans", sans-serif;
    overflow: hidden;
  }
  .brand-panel {
    position: absolute;
    left: 0; top: 0;
    width: 470px; height: 404px;
    background: var(--white);
  }
  .brand-name {
    position: absolute;
    left: 98px; top: 50px;
    width: 300px;
    text-align: center;
    font-size: 58px;
    font-weight: 400;
    color: var(--ink);
    letter-spacing: 1px;
  }
  .brand-tagline {
    position: absolute;
    left: 97px; top: 140px;
    width: 302px;
    text-align: center;
    font-size: 16.5px;
    font-weight: 400;
    color: var(--ink);
    letter-spacing: 0.2px;
  }
  .jewel {
    position: absolute;
  }
  .jewel--earring-left {
    left: 133px; top: 197px;
    width: 124px; height: 142px;
    border-radius: 50%;
    background: radial-gradient(circle at 50% 45%, #8b7cc0, var(--gem-violet) 60%, #4a4380);
  }
  .jewel--earring-right {
    left: 272px; top: 197px;
    width: 128px; height: 142px;
    border-radius: 50%;
    background: radial-gradient(circle at 50% 45%, #a78bc4, #8a6fae 55%, #6a69a8);
  }
  .jewel--bracelet {
    left: 0; top: 278px;
    width: 60px; height: 98px;
    border-radius: 0 30px 30px 0;
    background: linear-gradient(160deg, #d6b36a, var(--gem-gold) 55%, #8f6a26);
  }
  .sale-panel {
    position: absolute;
    left: 470px; top: 0;
    width: 730px; height: 404px;
    background:
      linear-gradient(170deg, var(--lav-2) 0%, var(--lav-1) 45%, var(--pink-1) 100%);
  }
  .jewel--ring {
    left: 1055px; top: 0;
    width: 140px; height: 150px;
    border-radius: 40% 40% 45% 45%;
    background: radial-gradient(circle at 50% 45%, #6b5a8c, var(--ring-dark) 55%, #8a6a2e 80%);
  }
  .sale-copy {
    position: absolute;
    left: 515px; top: 106px;
  }
  .sale-title {
    font-size: 52px;
    font-weight: 400;
    color: var(--white);
    line-height: 62px;
  }
  .sale-offer {
    margin-top: 4px;
    font-size: 36px;
    font-weight: 400;
    color: var(--plum);
    line-height: 48px;
  }
  .sale-code {
    font-size: 32px;
    font-weight: 400;
    color: var(--plum);
    line-height: 52px;
  }
  .sale-code__value {
    margin-left: 8px;
    font-weight: 600;
    color: var(--white);
    letter-spacing: 0.5px;
  }
</style>
</head>
<body>
  <div class="banner">
    <section class="brand-panel">
      <div class="brand-name">Brindlyx</div>
      <div class="brand-tagline">FINE ESTATE AND DESIGNER JEWELRY</div>
    </section>

    <div class="sale-panel" role="img" aria-label="Soft lavender photo of a waving American flag"></div>

    <div class="jewel jewel--bracelet" role="img" aria-label="Gold and diamond bracelet"></div>
    <div class="jewel jewel--earring-left" role="img" aria-label="Flower earring with purple and blue sapphire petals and diamond center"></div>
    <div class="jewel jewel--earring-right" role="img" aria-label="Flower earring with pink, violet and blue sapphire petals and diamond center"></div>
    <div class="jewel jewel--ring" role="img" aria-label="Large amethyst cocktail ring set in textured gold"></div>

    <div class="sale-copy">
      <h1 class="sale-title">Labor Day Sale</h1>
      <p class="sale-offer">Save 15% on Everything!</p>
      <p class="sale-code">Use Promo Code:<span class="sale-code__value">HALCYON</span></p>
    </div>
  </div>
</body>
</html>
```